Name my translations company

I am looking for a name for my translations company. (no logo).
I need a short name that is available in .com and pinwhirl.

To double check this please use this tool:
www.brindlelookup.com

Names that are not available in .com and pinwhirl are going to be rejected.

I prefer short names (5-8 letters).

some ideas:
put some letters like a, o , e at the end of some common names.
Use be at the beginning of the name
Use common phrases like say ok
It can include numbers ex: vort37 (domain taken).

Other ideas:
SunnyKettle (or a combination of 2 common names)

I don't want these words:
Chat

```html
<!DOCTYPE html>
<html lang="en">
<head>
<meta charset="utf-8">
<title>verbo36.com — We translate.</title>
<link rel="stylesheet" href="https://fonts.googleapis.com/css2?family=Noto+Serif:wght@700&family=Noto+Sans:ital@1&display=swap">
<style>
  :root {
    --sky-top: #e3a461;
    --sky-bottom: #fff6aa;
    --sun-top: #e2943f;
    --sun-bottom: #fbe687;
    --ink-navy: #10213f;
    --tagline-white: #ffffff;
  }
  html, body {
    margin: 0;
    padding: 0;
    overflow: hidden;
  }
  .canvas {
    position: relative;
    width: 1200px;
    height: 900px;
    overflow: hidden;
  }
  .backdrop {
    position: absolute;
    inset: 0;
    display: block;
  }
  .brand {
    position: absolute;
    left: 72px;
    top: 48px;
    margin: 0;
  }
  .brand-name {
    display: block;
    font-family: "Noto Serif", Georgia, serif;
    font-weight: 700;
    font-size: 92px;
    line-height: 1;
    letter-spacing: 0;
    color: var(--ink-navy);
  }
  .tagline {
    display: block;
    margin-top: 18px;
    font-family: "Noto Sans", Arial, sans-serif;
    font-style: italic;
    font-weight: 400;
    font-size: 39px;
    line-height: 1;
    letter-spacing: 1px;
    color: var(--tagline-white);
  }
</style>
</head>
<body>
<div class="canvas">
  <svg class="backdrop" width="1200" height="900" viewBox="0 0 1200 900" aria-hidden="true">
    <defs>
      <linearGradient id="sky-gradient" x1="0" y1="0" x2="0" y2="1">
        <stop offset="0" stop-color="var(--sky-top)"/>
        <stop offset="1" stop-color="var(--sky-bottom)"/>
      </linearGradient>
      <linearGradient id="sun-gradient" x1="0" y1="0" x2="0" y2="1">
        <stop offset="0" stop-color="var(--sun-top)"/>
        <stop offset="1" stop-color="var(--sun-bottom)"/>
      </linearGradient>
    </defs>
    <rect class="sky" width="1200" height="900" fill="url(#sky-gradient)"/>
    <ellipse class="sun-disc" cx="360" cy="328" rx="703" ry="474" fill="url(#sun-gradient)"/>
  </svg>
  <h1 class="brand">
    <span class="brand-name">verbo36.com</span>
    <span class="tagline">We translate.</span>
  </h1>
</div>
</body>
</html>
```